Law firm Seeks Modern and Engaging Site Redesign

Law firm seeks a new web site. Should be modern, but retaining existing logo. Needs to include contact section, professional bio, services offered, and contact information.

The site should be modern, responsive, and able to be SEO optimized.

The finished product should be coded in a Wordpress site, which I will provide. I can work with other platforms, including Wix, but WP is preferred.

Note the current site is https://www.tallowfieldlaw.example/#/home

Target Market(s)

Family Law Practice

Industry/Entity Type

Legal

Coding

Coded - Design and coding required

Number of Pages Required

4 page

Font styles to use
Sans Serif

Requirements
Must have
• Service description
Bio pages for partners
Contact Form
Awards/Publication page

```html
<!DOCTYPE html>
<html lang="en">
<head>
<meta charset="utf-8">
<title>Tallowfield Marsh — Attorneys at Law</title>
<link rel="stylesheet" href="https://fonts.googleapis.com/css2?family=Montserrat:wght@400;500;600&family=Ubuntu:wght@500;700&display=swap">
<style>
:root{
  --ink:#111;
  --header:#1d1d1d;
  --frame:#5e5e5e;
  --gold:#8d7a49;
  --blue:#3d5bd9;
  --footer:#3b3b3b;
  --white:#fff;
}
*{margin:0;padding:0;box-sizing:border-box}
html,body{width:1200px;height:2700px;overflow:hidden;background:var(--white)}
body{position:relative;font-family:"Montserrat",sans-serif;color:var(--ink)}
.abs{position:absolute}
.site-header{left:0;top:0;width:1200px;height:84px;background:var(--header)}
.brand{left:10px;top:16px;display:flex;align-items:flex-start;gap:10px;font-family:"Montserrat",sans-serif}
.brand-name{font-size:36px;font-weight:500;color:#8a8a8a;line-height:40px}
.brand-name .accent{color:#8a8a8a}
.brand-divider{width:4px;height:56px;background:var(--blue)}
.brand-tag{font-size:14px;color:#8a8a8a;margin-top:2px}
.main-nav{right:40px;top:28px;display:flex;align-items:center}
.main-nav a{color:var(--white);text-decoration:none;font-size:21px;padding:0 22px;border-left:4px solid var(--blue);line-height:38px}
.main-nav a:first-child{border-left:none}
.hero{left:0;top:84px;width:1200px;height:556px;background:linear-gradient(180deg,#2c2d33 0%,#6e5a44 45%,#a07f5b 70%,#7a5a3d 100%)}
.about-frame{left:0;top:640px;width:1200px;height:765px;background:var(--frame)}
.about-inner{left:16px;top:658px;width:1166px;height:729px;background:var(--white)}
.about-tab{left:287px;top:598px;width:627px;height:84px;background:var(--frame);color:var(--white);font-family:"Ubuntu",sans-serif;font-weight:700;font-size:56px;text-align:center;line-height:88px}
.justice-photo{left:47px;top:697px;width:449px;height:664px;background:radial-gradient(ellipse at 45% 55%,#6b5532 0%,#1f2a52 45%,#131a3a 100%)}
.about-copy{left:543px;top:762px;width:620px;font-size:21px;line-height:22.6px}
.about-copy p{margin-bottom:22.6px}
.attorneys-title{left:346px;top:1416px;width:505px;height:94px;border:11px solid var(--gold);font-family:"Ubuntu",sans-serif;font-weight:700;font-size:56px;text-align:center;line-height:70px}
.portrait{width:270px;height:330px;background:linear-gradient(180deg,#ffffff 0%,#d9d9dc 30%,#2e3040 60%,#3a2320 100%)}
.bio-card{width:353px;height:150px;border:7px solid var(--gold);border-bottom:none;background:var(--white);padding:12px 14px 0 18px;font-size:17.5px;line-height:19px}
.bio-card b{font-weight:600}
.bio-card .more{color:var(--blue);font-size:10px}
.bio-base{height:7px;background:var(--gold)}
.dots{display:flex;gap:9px}
.dots span{width:28px;height:28px;border-radius:50%;background:var(--gold);border:3px solid var(--white)}
.testimonial-title{left:0;top:2084px;width:1176px;text-align:center;font-size:29px;font-weight:500}
.quote{width:469px;height:92px;border:5px solid var(--gold);background:var(--white);box-shadow:4px 8px 10px rgba(0,0,0,.3);font-size:15px;line-height:20px;text-align:center;padding:10px 14px 0}
.quote-tail{width:22px;height:22px;background:var(--white);border-right:5px solid var(--gold);border-bottom:5px solid var(--gold);transform:rotate(45deg)}
.quote-name{font-size:15px}
.rule{left:0;top:2333px;width:1200px;height:2px;background:#777}
.map-area{left:0;top:2335px;width:1166px;height:236px;background:linear-gradient(90deg,#eceef0 0%,#e6e8ea 65%,#9fc8e8 72%,#d8e8d0 85%,#eceef0 100%)}
.site-footer{left:0;top:2606px;width:1200px;height:94px;background:var(--footer);color:var(--white)}
.footer-brand{left:34px;top:2614px;width:164px;height:40px;background:var(--white);display:flex;align-items:center;gap:6px;padding-left:8px;font-size:16px;color:#888}
.footer-brand i{width:2px;height:26px;background:var(--blue)}
.footer-address{left:34px;top:2659px;font-size:13px;line-height:14px;color:var(--white)}
.footer-phone{left:312px;top:2642px;display:flex;gap:12px;align-items:center;font-size:21px;line-height:18px}
.footer-mail{left:618px;top:2640px;display:flex;gap:10px;align-items:center;font-size:21px}
.quick{left:912px;top:2618px;font-size:21px}
.quick-links{left:955px;top:2650px;display:grid;grid-template-columns:110px 90px;font-size:18px;line-height:20px}
</style>
</head>
<body>
<header class="site-header abs">
  <div class="brand abs">
    <span class="brand-name">Tallowfield Marsh</span>
  </div>
  <nav class="main-nav abs">
    <a href="#">Home</a><a href="#">Services</a><a href="#">About</a><a href="#">Awards</a><a href="#">Contact</a>
  </nav>
</header>

<div class="hero abs" role="img" aria-label="Photo of a gavel and brass scales of justice on a desk with an attorney behind"></div>

<div class="about-frame abs"></div>
<div class="about-inner abs"></div>
<h2 class="about-tab abs">Who We Are</h2>
<div class="justice-photo abs" role="img" aria-label="Bronze statue of Lady Justice against a dark blue backdrop"></div>
<div class="about-copy abs">
  <p>The law firm of Tallowfield Marsh, LLC is based in Bergen County, conveniently located in Linden Vale, New Jersey in 14 Orchard Crossing. We serve the needs of clients throughout Bergen County, as well as, clients from several other counties, including, but not limited to, Passaic, Morris, Essex and Hudson. Between our partners, we have over 30+ years of experience assisting clients with all of their family law and criminal law needs.</p>
  <p>Often times the areas of family law and criminal law cross paths, which can be both emotionally and financially com-plex. We understand that our client's case is unique and pride ourselves on being responsive to all of our clients needs.</p>
  <p>Both Mr. Tallowfield and Mr. Marsh practiced privately for well over a decade as partners in two of Bergen County's most established Family Law firms before joining together to use their knowledge and experience to assist their cli-ents with all of their legal needs.</p>
  <p>Whether your needs are family or criminal law related, contact Tallowfield Marsh, LLC to schedule a consultation.</p>
</div>

<h2 class="attorneys-title abs">Our Attorneys</h2>

<div class="portrait abs" style="left:58px;top:1522px" role="img" aria-label="Portrait of a partner in a dark suit"></div>
<div class="portrait abs" style="left:438px;top:1540px" role="img" aria-label="Portrait of a partner seated at a desk"></div>
<div class="portrait abs" style="left:908px;top:1548px;width:258px" role="img" aria-label="Portrait of a partner seated in a leather chair"></div>

<div class="bio-card abs" style="left:39px;top:1852px"><b>Daniel R. Tallowfield</b> practices in the area of family law, specializing in high conflict matters relating to divorce, custody, equitable distri-bution, and complex financial is-sues........<span class="more">Know More</span></div>
<div class="bio-base abs" style="left:39px;top:1995px;width:162px"></div>
<div class="bio-base abs" style="left:352px;top:1995px;width:40px"></div>
<div class="dots abs" style="left:206px;top:1984px"><span></span><span></span><span></span><span></span></div>

<div class="bio-card abs" style="left:435px;top:1852px;padding-top:8px"><b>Daniel R. Tallowfield</b> practices in the area of family law, specializing in high conflict matters relating to divorce, custody, equitable distri-bution, and complex financial is-sues........<span class="more">Know More</span></div>
<div class="bio-base abs" style="left:435px;top:1995px;width:162px"></div>
<div class="bio-base abs" style="left:748px;top:1995px;width:40px"></div>
<div class="dots abs" style="left:602px;top:1984px"><span></span><span></span><span></span><span></span></div>

<div class="bio-card abs" style="left:823px;top:1852px"><b>Daniel R. Tallowfield</b> practices in the area of family law, specializing in high conflict matters relating to divorce, custody, equitable distri-bution, and complex financial is-sues........<span class="more">Know More</span></div>
<div class="bio-base abs" style="left:823px;top:1995px;width:162px"></div>
<div class="bio-base abs" style="left:1136px;top:1995px;width:40px"></div>
<div class="dots abs" style="left:990px;top:1984px"><span></span><span></span><span></span><span></span></div>

<h3 class="testimonial-title abs">Testimonial</h3>
<div class="quote abs" style="left:108px;top:2123px">It was great working with such an amazing team of people, There consultation is workth taking. There sevices has helped me for a very long period of time</div>
<div class="quote-tail abs" style="left:498px;top:2206px"></div>
<div class="quote-name abs" style="left:513px;top:2233px">-mara lenox</div>
<div class="quote abs" style="left:612px;top:2123px">It was great working with such an amazing team of people, There consultation is workth taking. There sevices has helped me for a very long period of time</div>
<div class="quote-tail abs" style="left:1002px;top:2206px"></div>
<div class="quote-name abs" style="left:1018px;top:2235px">-mara lenox</div>

<svg class="abs" style="left:1112px;top:2254px" width="86" height="62" viewBox="0 0 86 62" aria-label="Previous and next">
  <path d="M36 6 L12 31 L36 56" fill="none" stroke="#3a3a3a" stroke-width="12" stroke-linecap="round" stroke-linejoin="round"/>
  <path d="M50 6 L74 31 L50 56" fill="none" stroke="#3a3a3a" stroke-width="12" stroke-linecap="round" stroke-linejoin="round"/>
</svg>

<div class="rule abs"></div>
<div class="map-area abs" role="img" aria-label="Street map showing the office location near a university campus"></div>

<footer class="site-footer abs"></footer>
<div class="footer-brand abs"><span>Tallowfield</span><i></i><span>Marsh</span></div>
<div class="footer-address abs">14 Orchard Crossing Suite 210<br>Linden Vale, NJ 07999</div>
<div class="footer-phone abs">
  <svg width="34" height="34" viewBox="0 0 24 24" aria-hidden="true"><path d="M6.6 10.8a15 15 0 0 0 6.6 6.6l2.2-2.2a1 1 0 0 1 1-.25 11.4 11.4 0 0 0 3.6.57 1 1 0 0 1 1 1V20a1 1 0 0 1-1 1A17 17 0 0 1 3 4a1 1 0 0 1 1-1h3.5a1 1 0 0 1 1 1c0 1.25.2 2.45.57 3.57a1 1 0 0 1-.25 1z" fill="#fff"/></svg>
  <span>(555) 014-2271 Phone<br>(555) 014-2290 Fax</span>
</div>
<div class="footer-mail abs">
  <svg width="36" height="24" viewBox="0 0 36 24" aria-hidden="true"><rect x="1" y="1" width="34" height="22" fill="#fff"/><path d="M1 1 L18 14 L35 1" fill="none" stroke="#3b3b3b" stroke-width="2"/></svg>
  <span>T&amp;M@mail.example</span>
</div>
<svg class="abs" style="left:914px;top:2613px" width="36" height="36" viewBox="0 0 24 24" aria-hidden="true"><circle cx="12" cy="12" r="10" fill="none" stroke="#fff" stroke-width="1.6"/><ellipse cx="12" cy="12" rx="4.5" ry="10" fill="none" stroke="#fff" stroke-width="1.4"/><path d="M2 12h20M4 7h16M4 17h16" stroke="#fff" stroke-width="1.4"/></svg>
<div class="quick abs" style="left:956px;color:#fff">Quick Access</div>
<div class="quick-links abs" style="color:#fff"><span>Services</span><span>Awards</span><span>About</span><span>Contact</span></div>
</body>
</html>
```